Business Cards for Tech Company - uBrightowl

We would like new modern business cards designed for our company. Attached are some examples of other business cards we like. <br/><br/>Info we need is: <br/>First Name, Last Name<br/>Address<br/>Store Phone<br/>Cell Phone<br/>Email Address<br/>Text Logo <br/>And Other Logo<br/>

Industry/Entity Type

Technology Equipment

Contact Information for Business Card

Please use these details as example:

Dale Morrow
Technology Specialist
Direct 555.617.2094
Phone 555-730-8186

dale.morrow@ubrightowl.example

2971 Willet Lane
Alder Falls, OR 00427

Font styles to use
Sans Serif
Other font styles liked:
• Anything easy to read and modern

Colors

Designer to choose colors to be used in the design.

Requirements
Must have
• Both Logos
• Signature as name
• Use the text logo and use the shark logo but do not use the full shark logo. Have it where it is zoomed in and is expanding out of the card.
Nice to have
• Keep it clean and modern
• We like blue, white, and black/grays.
Should not have
• Random icons for phone and address.

```html
<!DOCTYPE html>
<html lang="en">
<head>
<meta charset="utf-8">
<title>uBrightowl Business Card</title>
<link href="https://fonts.googleapis.com/css2?family=Lato:wght@400;700;900&display=swap" rel="stylesheet">
<style>
  :root {
    --stage: #3a3430;
    --card: #050505;
    --decor-a: #2a2a2a;
    --decor-b: #151515;
    --blue: #3d8fd1;
    --white: #f2f2f2;
  }
  * { margin: 0; padding: 0; box-sizing: border-box; }
  html, body { width: 1200px; height: 847px; overflow: hidden; }
  body {
    background: var(--stage);
    font-family: "Lato", sans-serif;
    position: relative;
  }
  .card {
    position: absolute;
    top: 269px;
    width: 540px;
    height: 309px;
    background: var(--card);
    overflow: hidden;
    border-radius: 3px;
    box-shadow: 0 14px 30px rgba(0,0,0,.45);
  }
  .card--front { left: 40px; }
  .card--back { left: 620px; }

  .emblem-area {
    position: absolute;
    border-radius: 50%;
    background: radial-gradient(ellipse at center, var(--decor-a) 0%, var(--decor-b) 70%, transparent 72%);
  }
  .card--front .emblem-area { left: -40px; top: -60px; width: 260px; height: 420px; }
  .card--back .emblem-area { right: -70px; top: -10px; width: 250px; height: 380px; }

  .wordmark {
    position: absolute;
    left: 90px;
    top: 118px;
    display: flex;
    align-items: center;
    gap: 12px;
  }
  .wordmark__square { width: 18px; height: 18px; background: var(--blue); }
  .wordmark__name {
    font-weight: 900;
    font-size: 54px;
    color: var(--white);
    letter-spacing: -1px;
  }

  .identity {
    position: absolute;
    left: 50px;
    top: 96px;
  }
  .identity__name {
    font-weight: 900;
    font-size: 25px;
    color: var(--blue);
    text-transform: uppercase;
    letter-spacing: -.5px;
  }
  .identity__title { font-size: 15px; color: var(--white); margin-top: 2px; }

  .divider {
    position: absolute;
    left: 244px;
    top: 92px;
    width: 2px;
    height: 108px;
    background: var(--blue);
  }

  .contact {
    position: absolute;
    left: 262px;
    top: 90px;
    font-size: 14px;
    line-height: 21px;
    color: var(--white);
  }
  .contact__row { display: flex; align-items: center; gap: 8px; }
  .contact__row svg { width: 13px; height: 13px; flex: none; }

  .website {
    position: absolute;
    left: 50px;
    bottom: 50px;
    font-size: 16px;
    letter-spacing: 5px;
    color: var(--white);
  }
  .website__name { color: var(--blue); }
</style>
</head>
<body>
  <section class="card card--front">
    <div class="emblem-area" role="img" aria-label="Large faint close-up of the company emblem expanding off the card edge"></div>
    <div class="wordmark">
      <span class="wordmark__square"></span>
      <span class="wordmark__name">uBrightowl</span>
    </div>
  </section>

  <section class="card card--back">
    <div class="emblem-area" role="img" aria-label="Large faint close-up of the company emblem expanding off the card edge"></div>
    <div class="identity">
      <h1 class="identity__name">Dale Morrow</h1>
      <p class="identity__title">Technology Specialist</p>
    </div>
    <div class="divider"></div>
    <div class="contact">
      <p>2971 Willet Lane</p>
      <p>Alder Falls, OR 00427</p>
      <p class="contact__row">
        <svg viewBox="0 0 14 14" aria-hidden="true"><path d="M2 4 Q2 2 4 2 H10 Q12 2 12 4 V5 H9 V4 H5 V5 H2 Z M3 6 H11 L12 12 H2 Z" fill="var(--blue)"/><circle cx="7" cy="9" r="1.6" fill="var(--card)"/></svg>
        555.617.2094
      </p>
      <p class="contact__row">
        <svg viewBox="0 0 14 14" aria-hidden="true"><rect x="3.5" y="1" width="7" height="12" rx="1.2" fill="none" stroke="var(--blue)" stroke-width="1.4"/><rect x="6" y="10.5" width="2" height="1" fill="var(--blue)"/></svg>
        555-730-8186
      </p>
      <p class="contact__row">
        <svg viewBox="0 0 14 14" aria-hidden="true"><rect x="1" y="3" width="12" height="8" fill="var(--blue)"/><path d="M1 3 L7 8 L13 3" fill="none" stroke="var(--card)" stroke-width="1.2"/></svg>
        dale.morrow@ubrightowl.example
      </p>
    </div>
    <p class="website">www.<span class="website__name">ubrightowl</span>.com</p>
  </section>
</body>
</html>
```